Onboarding Carousel UI/UX design

We need a great UI/UX design for our onboarding carousel as attached in the PDF document. The chosen designers will be given our brand book with colors and styles to be used. The images must be focused on the content of each slide and be professional unique style (Do not use the childish cartoons we have used for placeholders)

Industry/Entity Type

Mortgage Brokerage

Number of Pages Required

5+ page

Other font styles liked:
• Roboto

Requirements
Must have
• Great UI / UX design
Very relevant content of the images to match the slide
Nice to have
• Brand book

https://proto.velmarink.com/view/a4c7e210-8b3f-4d19-a6e2-5f0c91b7d3e8-c2fa/?fullscreen

Image styles we like. Would need to be customized and made unique for us.

https://pixelmarsh.com/shots/4817302-Tarvo-Quillnet-Illustration-Collaboration
https://brackwellstudio.co.za/software-client-style-frames
Should not have
• Do not use the childish images we have used as placeholders

```html
<!DOCTYPE html>
<html lang="en">
<head>
<meta charset="utf-8">
<title>Onboarding Carousel</title>
<link rel="stylesheet" href="https://fonts.googleapis.com/css2?family=Roboto:wght@300;400;500;700&display=swap">
<style>
  :root {
    --canvas: #f0f0f0;
    --screen: #ffffff;
    --frame: #0e0f12;
    --ink: #14233c;
    --body: #6b7380;
    --brand: #0a5cc0;
    --dot: #5a9be3;
    --mint: #bdeedd;
    --teal: #2fd3a0;
    --navy: #1d3b66;
    --blue: #cfe0f6;
    --pink: #f6cfe3;
    --grey: #eef0f3;
  }
  * { box-sizing: border-box; margin: 0; padding: 0; }
  html, body { width: 1200px; height: 395px; overflow: hidden; }
  body {
    background: var(--canvas);
    font-family: "Roboto", sans-serif;
    position: relative;
  }
  .carousel {
    position: absolute;
    left: 37px; top: 30px;
    display: flex;
    gap: 38px;
  }
  .screen {
    position: relative;
    width: 158px; height: 336px;
    background: var(--screen);
    border: 3.5px solid var(--frame);
    border-radius: 22px;
    text-align: center;
  }
  .screen__art {
    position: absolute;
    left: 22px; top: 26px;
    width: 106px; height: 128px;
    border-radius: 6px;
  }
  .art--welcome { background: linear-gradient(160deg, var(--grey), var(--mint) 55%, var(--blue)); }
  .art--email   { background: linear-gradient(150deg, var(--blue), var(--grey) 50%, var(--mint)); }
  .art--secure  { background: linear-gradient(160deg, var(--mint), var(--grey) 50%, var(--pink)); }
  .art--verify  { background: linear-gradient(150deg, var(--blue), var(--pink) 70%, var(--grey)); }
  .art--profile { background: linear-gradient(170deg, var(--grey), var(--blue) 45%, var(--mint)); }
  .art--apply   { background: linear-gradient(150deg, var(--grey), var(--pink) 50%, var(--blue)); }
  .screen__title {
    position: absolute;
    left: 0; right: 0; top: 181px;
    color: var(--ink);
    font-size: 12.2px;
    line-height: 15.5px;
    letter-spacing: -0.1px;
  }
  .screen__title strong { font-weight: 500; display: block; }
  .screen__title span { font-weight: 400; display: block; }
  .screen__text {
    position: absolute;
    left: 4px; right: 4px; top: 220px;
    color: var(--body);
    font-size: 6.5px;
    line-height: 10.5px;
    font-weight: 300;
  }
  .pager {
    position: absolute;
    left: 0; right: 0; top: 251px;
    display: flex; justify-content: center; align-items: center;
    gap: 4.4px;
    height: 6px;
  }
  .pager__dot {
    width: 2.6px; height: 2.6px; border-radius: 50%;
    background: var(--dot);
  }
  .pager__dot--active {
    width: 4.4px; height: 4.4px;
    background: var(--brand);
    box-shadow: 0 0 0 0.8px #fff, 0 0 0 1.4px var(--brand);
  }
  .screen__hint {
    position: absolute;
    left: 0; right: 0; top: 263px;
    color: var(--brand);
    font-size: 4.7px;
    font-weight: 500;
  }
  .button {
    position: absolute;
    left: 48px; top: 288px;
    width: 55px; height: 21px;
    background: var(--brand);
    color: #fff;
    border-radius: 2px;
    font-size: 6.6px;
    font-weight: 700;
    line-height: 21px;
  }
  .screen__signin {
    position: absolute;
    left: 0; right: 0; top: 315px;
    font-size: 5.5px;
    color: var(--ink);
  }
  .screen__signin a { color: var(--brand); text-decoration: none; }
</style>
</head>
<body>
<main class="carousel">

  <section class="screen">
    <div class="screen__art art--welcome" role="img" aria-label="Illustration: man holding a phone beside chat bubbles and a checklist form"></div>
    <h2 class="screen__title"><strong>Welcome to Finance</strong><span>Brokers Apply Online</span></h2>
    <p class="screen__text">You can apply online for your next<br>mortgage credit in about 20 minutes.</p>
    <div class="pager"><i class="pager__dot pager__dot--active"></i><i class="pager__dot"></i><i class="pager__dot"></i><i class="pager__dot"></i><i class="pager__dot"></i><i class="pager__dot"></i></div>
    <p class="screen__hint">It's easy, and we will guide you all the way.</p>
    <div class="button">Next</div>
    <p class="screen__signin">Have an Account? <a href="#">Sign In</a></p>
  </section>

  <section class="screen">
    <div class="screen__art art--email" role="img" aria-label="Illustration: man sitting with a phone next to an open email envelope"></div>
    <h2 class="screen__title"><strong>#1 Create Your</strong><span>Personal Account</span></h2>
    <p class="screen__text">You will need a valid email address<br>to create your account</p>
    <div class="pager"><i class="pager__dot"></i><i class="pager__dot pager__dot--active"></i><i class="pager__dot"></i><i class="pager__dot"></i><i class="pager__dot"></i><i class="pager__dot"></i></div>
    <p class="screen__hint">We will send you a confirmation email</p>
    <div class="button">Next</div>
    <p class="screen__signin">Have an Account? <a href="#">Sign In</a></p>
  </section>

  <section class="screen">
    <div class="screen__art art--secure" role="img" aria-label="Illustration: woman with a phone beside a large phone screen and a padlock shield"></div>
    <h2 class="screen__title"><strong>#2 Secure Your Account</strong><span>With Your Mobile Phone</span></h2>
    <p class="screen__text">You will need a valid mobile phone number<br>to enable two factor authentication.</p>
    <div class="pager"><i class="pager__dot"></i><i class="pager__dot"></i><i class="pager__dot pager__dot--active"></i><i class="pager__dot"></i><i class="pager__dot"></i><i class="pager__dot"></i></div>
    <p class="screen__hint">We will send you a confirmation email</p>
    <div class="button">Next</div>
    <p class="screen__signin">Have an Account? <a href="#">Sign In</a></p>
  </section>

  <section class="screen">
    <div class="screen__art art--verify" role="img" aria-label="Illustration: woman reclining with a phone in front of a verified identity card and a shield"></div>
    <h2 class="screen__title"><strong>#3 Verify Your</strong><span>Identity Online</span></h2>
    <p class="screen__text">You will need to have a valid<br>Romanian ID card or residence permit</p>
    <div class="pager"><i class="pager__dot"></i><i class="pager__dot"></i><i class="pager__dot"></i><i class="pager__dot pager__dot--active"></i><i class="pager__dot"></i><i class="pager__dot"></i></div>
    <p class="screen__hint">You will take a photo of your card</p>
    <div class="button">Next</div>
    <p class="screen__signin">Have an Account? <a href="#">Sign In</a></p>
  </section>

  <section class="screen">
    <div class="screen__art art--profile" role="img" aria-label="Illustration: man with a tablet in front of a profile form with ticked items"></div>
    <h2 class="screen__title"><strong>#4 Create Your Profile</strong><span>Data For The Application</span></h2>
    <p class="screen__text">Tell us about your current situation including<br>employment, income,assets and liabilities</p>
    <div class="pager"><i class="pager__dot"></i><i class="pager__dot"></i><i class="pager__dot"></i><i class="pager__dot"></i><i class="pager__dot pager__dot--active"></i><i class="pager__dot"></i></div>
    <p class="screen__hint">You will take a photo of your card</p>
    <div class="button">Next</div>
    <p class="screen__signin">Have an Account? <a href="#">Sign In</a></p>
  </section>

  <section class="screen">
    <div class="screen__art art--apply" role="img" aria-label="Illustration: jumping woman beside charts and a target hit by a dart"></div>
    <h2 class="screen__title"><strong>#5 Apply For The Right</strong><span>Loan For Your Needs</span></h2>
    <p class="screen__text">You will be presented with your options,<br>upload any supporting documents</p>
    <div class="pager"><i class="pager__dot"></i><i class="pager__dot"></i><i class="pager__dot"></i><i class="pager__dot"></i><i class="pager__dot"></i><i class="pager__dot pager__dot--active"></i></div>
    <p class="screen__hint">You will take a photo of your card</p>
    <div class="button">Next</div>
    <p class="screen__signin">Have an Account? <a href="#">Sign In</a></p>
  </section>

</main>
</body>
</html>
```